Commercial Construction Company

We need a business card design based on our current logo. We are a commercial general contractor based in Southern California that specializes in bank remodels. We would like to see designs that incorporate dark blue. The final design should portray an image of professionalism and quality.

If possible, I would like to add metallic foil to the design. Thank you

```html
<!DOCTYPE html>
<html lang="en">
<head>
<meta charset="UTF-8">
<title>Harlan Commercial – Business Card</title>
<link rel="stylesheet" href="https://fonts.googleapis.com/css2?family=Oswald:wght@600&family=Montserrat:wght@400;500;600&display=swap">
<style>
  :root {
    --backdrop: #161616;
    --card: #242424;
    --card-edge: #2c2c2c;
    --foil: #a9a9a9;
    --ink: #5c5c5c;
    --ink-soft: #4e4e4e;
  }
  * { box-sizing: border-box; margin: 0; padding: 0; }
  html, body {
    width: 1200px; height: 900px; overflow: hidden;
    background: var(--backdrop);
    font-family: "Montserrat", sans-serif;
  }
  .stage {
    width: 1200px; height: 900px;
    display: flex; flex-direction: column; align-items: center; justify-content: center;
    gap: 40px;
  }
  .card {
    position: relative;
    width: 680px; height: 388px;
    background: var(--card);
    border: 1px solid var(--card-edge);
    box-shadow: 0 14px 30px rgba(0,0,0,.55);
  }
  /* Front */
  .card--front { display: flex; align-items: center; justify-content: center; }
  .brand { display: flex; align-items: center; gap: 18px; color: var(--foil); }
  .brand__dot { width: 26px; height: 26px; border-radius: 50%; background: var(--foil); }
  .brand__name {
    font-family: "Montserrat", sans-serif; font-weight: 600;
    font-size: 30px; line-height: 1.15; letter-spacing: .04em; text-transform: uppercase;
  }
  /* Back */
  .identity {
    position: absolute; left: 78px; top: 128px; width: 250px; text-align: right;
  }
  .identity__name {
    font-family: "Oswald", sans-serif; font-weight: 600;
    font-size: 40px; letter-spacing: .01em; color: var(--ink); text-transform: uppercase; line-height: 1.05;
  }
  .identity__role { font-size: 17px; color: var(--ink-soft); margin-top: 2px; }
  .divider {
    position: absolute; left: 350px; top: 130px; width: 2px; height: 72px; background: var(--ink-soft);
  }
  .contacts {
    position: absolute; left: 378px; top: 126px; list-style: none;
    font-size: 19px; color: var(--ink); line-height: 1.5;
  }
  .contacts li { display: flex; align-items: center; gap: 12px; }
  .contacts svg { width: 14px; height: 14px; flex: none; }
  .address {
    position: absolute; left: 0; right: 0; bottom: 52px; text-align: center;
    font-size: 19px; color: var(--ink); letter-spacing: .01em;
  }
</style>
</head>
<body>
<main class="stage">
  <section class="card card--front" aria-label="Card front">
    <div class="brand">
      <span class="brand__dot"></span>
      <span class="brand__name">Harlan Commercial<br>Construction Services</span>
    </div>
  </section>

  <section class="card card--back" aria-label="Card back">
    <div class="identity">
      <p class="identity__name">Martin Keller</p>
      <p class="identity__role">Director</p>
    </div>
    <span class="divider"></span>
    <ul class="contacts">
      <li>
        <svg viewBox="0 0 16 16" fill="none" stroke="var(--ink)" stroke-width="1.8" stroke-linecap="round"><path d="M4 1.5 6 5 4.5 6.5c1 2 3 4 5 5L11 10l3.5 2-1 2.5C8 15 1 8 1.5 2.5z"/></svg>
        (555) 014-2290
      </li>
      <li>
        <svg viewBox="0 0 16 16" fill="none" stroke="var(--ink)" stroke-width="1.6"><rect x="1.5" y="3.5" width="13" height="9"/><path d="M1.5 3.5 8 9l6.5-5.5"/></svg>
        info@harlanbuild.com
      </li>
      <li>
        <svg viewBox="0 0 16 16" fill="none" stroke="var(--ink)" stroke-width="1.4"><circle cx="8" cy="8" r="6.5"/><ellipse cx="8" cy="8" rx="2.8" ry="6.5"/><path d="M1.5 8h13"/></svg>
        www.harlanbuild.com
      </li>
    </ul>
    <p class="address">1187 Cedar Crest Lane Salem, OR 97302</p>
  </section>
</main>
</body>
</html>
```